Binder design for a veterinary clinic

We are seeking a talented designer to create a standout design for ring binders specifically for our veterinary clinic. These binders will be used to organize materials from our Continuing Professional Development (CPD) projects for colleagues and interns. The design should be clean, professional, and align with our brand guidelines. To give you a better understanding of our branding, we’ve included the design of our vehicles as a reference. As additional reference, please visit www.tierpraxolend.at

Target Market(s)

veterinarians

Industry/Entity Type

Veterinary

Font styles to use
Sans Serif

Colors
0054AA
0677BA
7BADD7
CADEEF
E8F1F8
FFC000
F8CF3A
FAE287
FDF2CF
FEFAEE

Requirements
Must have
• Our Logo an a clean design
Should not have
• to much images

```html
<!DOCTYPE html>
<html lang="de">
<head>
<meta charset="utf-8">
<title>Tierpraxolend – Ordner</title>
<link rel="stylesheet" href="https://fonts.googleapis.com/css2?family=Montserrat:wght@700;800&display=swap">
<style>
  :root {
    --navy: #243646;
    --green: #18a574;
    --green-soft: #58b18b;
    --gold: #d49f2a;
    --white: #ffffff;
  }
  * { margin: 0; padding: 0; box-sizing: border-box; }
  html, body { width: 1200px; height: 637px; overflow: hidden; background: var(--white); }
  .binder {
    position: relative;
    width: 1200px;
    height: 637px;
    background: var(--navy);
    font-family: "Montserrat", sans-serif;
    overflow: hidden;
  }
  .back-cover { position: absolute; left: 0; top: 0; width: 652px; height: 637px; }
  .decor-circle {
    position: absolute;
    left: 3px; top: 324px;
    width: 316px; height: 316px;
    border-radius: 50%;
    background: var(--green-soft);
  }
  .spine-mark {
    position: absolute;
    left: 571px; top: 56px;
    width: 58px; height: 58px;
    border-radius: 50%;
    background: var(--white);
    border: 2px solid var(--gold);
  }
  .spine-title {
    position: absolute;
    left: 600px; top: 269px;
    transform: translate(-50%, -50%) rotate(-90deg);
    white-space: nowrap;
    color: var(--gold);
    font-weight: 800;
    font-size: 30px;
    letter-spacing: -0.5px;
  }
  .ring-hole {
    position: absolute;
    left: 573px; top: 425px;
    width: 54px; height: 54px;
    border-radius: 50%;
    background: var(--white);
  }
  .front-cover { position: absolute; left: 652px; top: 0; width: 548px; height: 637px; }
  .band-top { position: absolute; left: 0; top: 0; width: 100%; height: 116px; background: var(--green); }
  .band-bottom { position: absolute; left: 0; top: 576px; width: 100%; height: 61px; background: var(--green); }
  .brand {
    position: absolute;
    left: 297px; top: 38px;
    display: flex;
    align-items: center;
    gap: 11px;
  }
  .brand-mark {
    width: 65px; height: 65px;
    border-radius: 50%;
    background: var(--white);
    border: 2px solid var(--gold);
    flex: none;
  }
  .brand-name {
    color: var(--navy);
    font-weight: 800;
    font-size: 21px;
    line-height: 1;
    letter-spacing: -0.4px;
  }
  .brand-tagline {
    margin-top: 3px;
    color: var(--gold);
    font-weight: 700;
    font-size: 9.5px;
    line-height: 1;
  }
</style>
</head>
<body>
<main class="binder">
  <section class="back-cover">
    <div class="decor-circle" role="img" aria-label="Große Bildmarke der Klinik mit Hund und Katze als Dekoration"></div>
    <div class="spine-mark" aria-hidden="true"></div>
    <div class="spine-title">Tierpraxolend</div>
    <div class="ring-hole" aria-hidden="true"></div>
  </section>
  <section class="front-cover">
    <div class="band-top">
      <div class="brand">
        <div class="brand-mark" aria-hidden="true"></div>
        <div class="brand-text">
          <div class="brand-name">Tierpraxolend</div>
          <div class="brand-tagline">Fachklinik für Kleintiere</div>
        </div>
      </div>
    </div>
    <div class="band-bottom"></div>
  </section>
</main>
</body>
</html>
```